I need a flyer made , the flyer can be one page or two pages or three pages . I will be posting this on Instagram and social media platforms. I am a luxury home builder , I am looking to hire a construction project manager . Below are some examples and ideas what can be on the flyer

We’re looking for a construction project manager who’s passionate about building luxury homes at the highest standards
We’re hiring construction project manager
* Experience 5+ years in residential project management with a strong portfolio of completed homes.
* location : Bergen County NJ
* excellent leadership skills, leads teams with confidence and clarity
* communicates seamlessly with architects , engineers, designers and clients
*knows how to manage budgets and timelines without compromising quality
*solves problems with a positive solution first mindset
* pays attention to every detail because in luxury the small things are the big things

Apply now , link in bio or DM to connect.

My logo is attached, my web site www.ridgelanebuilders.com
My style is modern but still warm and inviting. I like a clean classy look .
Updates

Please don’t add any images of chairs or people to the flyer , I do not want people on my flyer. Do not add standard images of offices and houses , we are luxury builders , we build homes over 2 million dollars. Keep a classy , simple modern look . High end .

You can add a white hard hat with my logo on it for a image , this is a suggestion does not have to be on my flyer ,

```html
<!DOCTYPE html>
<html lang="en">
<head>
<meta charset="utf-8">
<title>Ridge Lane Builders — We're Hiring: Construction Project Manager</title>
<link rel="stylesheet" href="https://fonts.googleapis.com/css2?family=Tinos:ital,wght@0,400;0,700;1,700&family=Roboto+Condensed:wght@400;700&family=Roboto:wght@400;900&display=swap">
<style>
  :root {
    --ink: #0b0b0b;
    --text: #1c1c1c;
    --red: #e2232a;
    --white: #ffffff;
    --logo: #cfcfcf;
    --rule: #c4c6c8;
    --url: #2a2a2a;
  }
  * { margin: 0; padding: 0; box-sizing: border-box; }
  html, body { width: 927px; height: 1200px; overflow: hidden; background: var(--white); }
  .flyer {
    position: relative;
    width: 927px;
    height: 1200px;
    overflow: hidden;
    font-family: "Roboto Condensed", "Arial Narrow", sans-serif;
    color: var(--text);
  }
  .backdrop {
    position: absolute;
    inset: 0;
    background:
      linear-gradient(180deg, rgba(255,255,255,0) 70%, rgba(40,48,66,0.12) 100%),
      linear-gradient(90deg, #eceeef 0%, #f5f6f6 40%, #eef1f3 58%, #d6e5f1 62%, #b8d2e8 78%, #c9ddec 100%);
  }
  .bubble { position: absolute; left: 0; top: 0; width: 927px; height: 460px; }
  .brand {
    position: absolute;
    left: 61px;
    top: 46px;
    font-family: "Tinos", "Times New Roman", serif;
    font-weight: 400;
    font-size: 24px;
    letter-spacing: 0.06em;
    color: var(--logo);
  }
  .headline-lead {
    position: absolute;
    left: 482px;
    top: 40px;
    transform: translateX(-50%);
    font-family: "Tinos", "Times New Roman", serif;
    font-size: 60px;
    line-height: 1;
    color: var(--white);
  }
  .headline {
    position: absolute;
    left: 180px;
    top: 98px;
    font-family: "Tinos", "Times New Roman", serif;
    font-size: 170px;
    line-height: 1;
    letter-spacing: -0.01em;
    color: var(--white);
    white-space: nowrap;
  }
  .headline .bang {
    color: var(--red);
    font-weight: 700;
    font-style: italic;
    margin-left: -4px;
  }
  .role { position: absolute; left: 54px; top: 410px; width: 457px; text-align: center; }
  .role-kicker {
    font-family: "Tinos", "Times New Roman", serif;
    font-size: 28px;
    line-height: 1;
    letter-spacing: 0.01em;
    color: var(--text);
  }
  .role-title {
    margin-top: 8px;
    font-family: "Tinos", "Times New Roman", serif;
    font-size: 47px;
    line-height: 1;
    color: var(--ink);
    white-space: nowrap;
  }
  .role-rule { position: absolute; left: 55px; top: 501px; width: 456px; height: 5px; background: var(--ink); }
  .requirements { position: absolute; left: 54px; top: 520px; width: 455px; list-style: none; }
  .requirements li {
    border-bottom: 1px solid var(--rule);
    font-size: 18.5px;
    line-height: 24px;
    color: var(--text);
  }
  .req-experience { height: 71px; padding-top: 3px; }
  .req-experience .lead { font-size: 28px; }
  .req-location { height: 61px; padding-top: 14px; font-size: 24px !important; }
  .req-location strong { font-weight: 700; }
  .req-leadership { height: 71px; padding-top: 11px; }
  .req-communication { height: 72px; padding-top: 11px; }
  .req-budget { height: 69px; padding-top: 10px; }
  .req-problems { height: 48px; padding-top: 10px; }
  .req-detail { height: 75px; padding-top: 10px; }
  .apply { position: absolute; left: 98px; top: 1032px; width: 294px; height: 66px; }
  .website {
    position: absolute;
    left: 55px;
    top: 1128px;
    font-family: "Roboto", Arial, sans-serif;
    font-size: 20px;
    letter-spacing: 0.27em;
    color: var(--url);
  }
</style>
</head>
<body>
<main class="flyer">
  <div class="backdrop" role="img" aria-label="Soft-focus photo of a professional in a light blue shirt extending a hand for a handshake"></div>

  <svg class="bubble" viewBox="0 0 927 460" aria-hidden="true">
    <path d="M0 0 H927 V315 C862 350 790 373 732 384 L649 440 L666 388 C420 402 150 330 0 167 Z" fill="var(--ink)"/>
  </svg>

  <div class="brand">RIDGE LANE BUILDERS</div>

  <h1>
    <span class="headline-lead">We’re</span>
    <span class="headline">HIRING<span class="bang">!</span></span>
  </h1>

  <header class="role">
    <p class="role-kicker">CONSTRUCTION</p>
    <h2 class="role-title">PROJECT MANAGER</h2>
  </header>
  <div class="role-rule"></div>

  <ul class="requirements">
    <li class="req-experience"><span class="lead">Experience 5+</span> years in residential project<br>management with a strong portfolio of completed homes.</li>
    <li class="req-location"><strong>LOCATION</strong> : Bergen County NJ</li>
    <li class="req-leadership">Excellent leadership skills,<br>leads teams with confidence and clarity</li>
    <li class="req-communication">Communicates seamlessly with architects ,<br>engineers, designers and clients</li>
    <li class="req-budget">Knows how to manage budgets and timelines<br>without compromising quality</li>
    <li class="req-problems">Solves problems with a positive solution first mindset</li>
    <li class="req-detail">Pays attention to every detail because in luxury the<br>small things are the big things</li>
  </ul>

  <svg class="apply" viewBox="0 0 294 66" role="img" aria-label="Apply now">
    <path d="M10 0 H258 L272 66 H10 A10 10 0 0 1 0 56 V10 A10 10 0 0 1 10 0 Z" fill="var(--ink)"/>
    <path d="M158 3 H282 L294 30 L280 58 H158 L170 30 Z" fill="var(--red)"/>
    <text x="17" y="45" font-family="Roboto, Arial, sans-serif" font-weight="900" font-size="37" fill="var(--white)">APPLY</text>
    <text x="174" y="45" font-family="Roboto, Arial, sans-serif" font-weight="900" font-size="37" fill="var(--white)">NOW!</text>
  </svg>

  <p class="website">WWW.RIDGELANEBUILDERS.COM</p>
</main>
</body>
</html>
```